Float and wellness centre needs a website refresh

Our float and wellness centre has been operating in Brisbane, Australia for 3 months. Our website is functional and easy to use, but it lacks a compelling visual experience that sells our awesome services to our customers.<br/><br/>We would like a complete redesign of our webpage. It is very important that the redesign considers the page layout for mobile users and the winning design will need to show both a desktop and mobile version of each of the pages listed below.<br/><br/>Out current website can be found at https://www.ebbtidehaven.com.au/<br/><br/>The winning design will need to provide proposals for redesigning the 4 pages listed below:<br/>Home Page - https://www.ebbtidehaven.com.au/<br/>Float Page - https://www.ebbtidehaven.com.au/services/float<br/>Build Gift Card page - https://www.ebbtidehaven.com.au/giftcard/stepone?location=kelsworth<br/>Booking Page - https://www.ebbtidehaven.com.au/Calendar/Day?centerId=kelsworth&selectedCategory=FLOAT&date=12/18/2019%2000:00:00%20+10:00&sessionLength=60<br/><br/>We only need the 4 pages listed above as our web developer will use the assets from the above pages to standardize all the other pages in the site. It is very important your proposed pages contain the same information as our current pages so that we can properly see the complete layout.<br/><br/>The Home page must display the business logo in some way. We would like the website to have a white background and for it make tasteful use of color to highlight key features on the pages. Where color is used it should harmonize with the business logo. The website needs to feel bright, simple and relaxing. Our current site does not use images very well and we have had professional photos taken of the center and the float rooms specifically for this website project. You can download these, and the business logo images here: http://ebbtidehaven.com.au/websiteimages.zip <br/><br/>We have included a few links below to other centers who have pages that we like: <br/><br/>https://www.drifthollowpods.com/ <br/>https://www.quietnook.com.au/ <br/>https://www.moonbaysoak.com.au/<br/>

Industry/Entity Type

Health And Wellness

Number of Pages Required

4 page

Font styles to use
Sans Serif

Colors

Designer to choose colors to be used in the design.

Requirements
Must have
• It is very important your proposed pages contain the same information as our current pages so that we can properly see the complete layout.
• The Home page must display the business logo in some way.
• Where color is used it should harmonize with the business logo.
Nice to have
• The website needs to feel bright, simple and relaxing. Our current site does not use images very well and we have had professional photos taken of the center and the float rooms specifically for this website project. You can download these, and the business logo images here: http://ebbtidehaven.com.au/websiteimages.zip
Should not have
• Dark pages.

```html
<!DOCTYPE html>
<html lang="en">
<head>
<meta charset="utf-8">
<title>Ebbtide Haven – Float &amp; Wellness</title>
<link href="https://fonts.googleapis.com/css2?family=Montserrat:wght@400;500;600;700&family=Mulish:wght@400;600;700&display=swap" rel="stylesheet">
<style>
:root{
  --navy:#1c2766;
  --purple:#a556a9;
  --blue:#6d82d3;
  --footer:#7082d0;
  --orange:#f79a3e;
  --red:#e8356b;
  --text:#3a3f55;
  --line:#e3e4ec;
  --white:#ffffff;
}
*{box-sizing:border-box;margin:0;padding:0}
html,body{width:1200px;height:3373px;overflow:hidden}
body{font-family:"Mulish",sans-serif;color:var(--text);background:var(--white);position:relative}
.abs{position:absolute}
.heading{font-family:"Montserrat",sans-serif;font-weight:400;color:var(--navy);font-size:31px;letter-spacing:.5px;text-align:center}
.heading b{font-weight:700}
.heading::after{content:"";display:block;width:42px;height:2px;background:var(--orange);margin:14px auto 0}
.btn{display:inline-flex;align-items:center;gap:12px;height:30px;padding:0 4px 0 17px;border-radius:15px;
  background:linear-gradient(90deg,var(--orange),var(--red));color:#fff;font-family:"Montserrat",sans-serif;
  font-size:11px;font-weight:600;letter-spacing:.3px;text-transform:uppercase}
.btn .dot{width:22px;height:22px;border-radius:50%;background:#fff;display:flex;align-items:center;justify-content:center}

/* hero */
.hero{left:0;top:0;width:1200px;height:564px;background:linear-gradient(160deg,#d9d3c9 0%,#b9b4ad 45%,#8c8a86 100%)}
.hero-shade{left:0;top:0;width:1200px;height:564px;background:linear-gradient(180deg,rgba(40,40,60,.15),rgba(40,40,60,.25))}
.topbar{right:142px;top:10px;display:flex;gap:16px;align-items:center;color:#fff;font-size:12px;font-weight:600}
.topbar span{display:flex;align-items:center;gap:6px}
.topbar .sep{width:1px;height:16px;background:rgba(255,255,255,.7)}
.logo-box{left:141px;top:0;width:88px;height:105px;background:#fff;border-radius:0 0 6px 6px;display:flex;flex-direction:column;align-items:center;justify-content:center;gap:6px}
.logo-box .mark{width:34px;height:34px;border-radius:50%;background:var(--purple)}
.logo-box .name{font-family:"Montserrat",sans-serif;font-size:11px;font-weight:600;color:var(--navy);text-align:center;line-height:1.1}
.nav{left:360px;top:48px;display:flex;gap:22px;color:#fff;font-family:"Montserrat",sans-serif;font-size:13px;align-items:center}
.hero-copy{left:0;top:214px;width:1200px;text-align:center;color:#fff}
.hero-copy .welcome{font-family:"Montserrat",sans-serif;font-size:29px;font-weight:600;letter-spacing:.5px}
.hero-copy h1{font-family:"Montserrat",sans-serif;font-size:60px;font-weight:700;line-height:1.1;letter-spacing:1px}
.hero-copy p{font-size:17px;font-weight:600;line-height:30px;margin-top:6px}
.hero-copy .btn{margin-top:14px}
.scroll-tab{left:560px;top:532px;width:80px;height:40px;background:#fff;border-radius:40px 40px 0 0}

/* mission */
.mission{left:0;top:612px;width:1200px;text-align:center}
.mission .lead{font-size:12px;line-height:21px;margin-top:26px;color:#444}
.mission .sub{font-size:14.5px;line-height:21px;margin-top:10px;color:#222}
.mission .btn{margin-top:24px}

/* quick booking */
.quick{left:0;top:883px;width:1200px;height:267px}
.quick .photo{left:560px;top:0;width:640px;height:267px;background:linear-gradient(100deg,#e9e4dc,#cfc7bb 60%,#8fa48d)}
.quick .band{left:0;top:0;width:700px;height:267px;background:linear-gradient(180deg,var(--purple),var(--blue));clip-path:polygon(0 0,690px 0,600px 130px,680px 267px,0 267px)}
.quick .copy{left:143px;top:48px;color:#fff}
.quick h2{font-family:"Montserrat",sans-serif;font-size:30px;font-weight:400}
.quick h2 b{font-weight:700}
.quick h2::after{content:"";display:block;width:42px;height:2px;background:var(--orange);margin-top:14px}
.quick p{font-size:14.5px;line-height:21px;font-weight:600;margin-top:28px;width:420px}
.quick .btn{margin-top:18px}

/* services */
.services-title{left:0;top:1198px;width:1200px}
.card{top:1272px;width:212px;height:262px;border:1px solid var(--line);border-radius:4px;text-align:center;background:#fff}
.card .img{height:133px;border-radius:4px 4px 0 0}
.card .icon{width:50px;height:50px;border-radius:50%;background:#fff;margin:-27px auto 0;box-shadow:0 2px 6px rgba(0,0,0,.15);display:flex;align-items:center;justify-content:center}
.card h3{font-family:"Montserrat",sans-serif;font-size:14px;font-weight:600;color:#222;margin-top:10px}
.card p{font-size:12px;line-height:21px;color:#555;margin:8px 16px 0}

/* gift */
.gift{left:0;top:1591px;width:1200px;height:267px}
.gift .photo{left:0;top:0;width:640px;height:267px;background:linear-gradient(90deg,#9fb48e,#e8e3de 45%,#d9d2c8)}
.gift .band{left:520px;top:0;width:680px;height:267px;background:linear-gradient(180deg,var(--purple),var(--blue));clip-path:polygon(43px 0,100% 0,100% 100%,3px 100%,82px 130px)}
.gift .copy{right:141px;top:50px;color:#fff;text-align:right}
.gift h2{font-family:"Montserrat",sans-serif;font-size:30px;font-weight:400}
.gift h2 b{font-weight:700}
.gift h2::after{content:"";display:block;width:42px;height:2px;background:var(--orange);margin:14px 0 0 auto}
.gift p{font-size:14.5px;line-height:21px;font-weight:600;margin-top:28px}
.gift .btn{margin-top:14px}

/* hours & pricing */
.hp-title{left:0;top:1906px;width:1200px}
.table{top:1981px;width:448px;height:414px;border:1px solid var(--line);border-radius:4px;overflow:hidden}
.table .head{height:175px;display:flex;align-items:center;justify-content:center;color:#fff;font-family:"Montserrat",sans-serif;font-size:30px;font-weight:700;background:linear-gradient(180deg,rgba(165,86,169,.85),rgba(120,110,200,.85)),linear-gradient(120deg,#d8d2cc,#a9a6b0)}
.table .grid{display:grid;grid-template-columns:1fr 1fr}
.table .cell{border-right:1px solid var(--line);border-top:1px solid var(--line);display:flex;flex-direction:column;align-items:center;justify-content:center;text-align:center}
.table .cell:nth-child(2n){border-right:none}
.table .cell h4{font-family:"Montserrat",sans-serif;font-size:14.5px;font-weight:600;color:var(--navy)}
.table .cell span{font-size:12px;color:#333;margin-top:6px;line-height:17px}
.hours .cell{height:118px}
.pricing .cell{height:80px}

/* map + contact */
.map{left:0;top:2467px;width:1200px;height:477px;background:linear-gradient(135deg,#e9d8ea,#dcd6ec 50%,#d8e0ef)}
.contact{left:283px;top:2717px;width:634px;height:362px;background:#fff;border-radius:4px;box-shadow:0 4px 18px rgba(0,0,0,.08);z-index:5}
.contact .heading{margin-top:30px}
.field{position:absolute;border:1px solid #d6d8e0;height:33px;font-size:10px;color:#666;padding:9px 14px}
.contact .btn{position:absolute;left:268px;top:309px}

/* footer */
.footer{left:0;top:2944px;width:1200px;height:429px;background:var(--footer);color:#fff;z-index:1}
.flogo{left:141px;top:180px;text-align:center}
.flogo .mark{width:60px;height:60px;border-radius:50%;background:rgba(255,255,255,.85);margin:0 auto 10px}
.flogo .name{font-family:"Montserrat",sans-serif;font-size:17px;font-weight:600}
.fdiv{width:1px;background:rgba(255,255,255,.35);top:168px;height:174px}
.fcol{top:180px}
.fcol h5{font-family:"Montserrat",sans-serif;font-size:14.5px;font-weight:600;margin-bottom:10px}
.fcol li{list-style:none;font-size:12px;line-height:22.5px}
.crow{display:flex;gap:14px;font-size:11px;line-height:17px;margin-bottom:10px;align-items:flex-start}
.subscribe{width:225px;height:34px;border:1px solid rgba(255,255,255,.8);border-radius:17px;display:flex;align-items:center;justify-content:space-between;padding:0 3px 0 13px;font-size:10px}
.subscribe .go{width:28px;height:28px;border-radius:50%;background:linear-gradient(90deg,var(--orange),var(--red))}
.social{display:flex;gap:10px;margin-top:14px}
.social span{width:24px;height:24px;border:1px solid #fff;border-radius:50%}
.copyright{left:0;top:386px;width:1200px;border-top:1px solid rgba(255,255,255,.35);text-align:center;font-size:12px;padding-top:12px}
</style>
</head>
<body>

<!-- Hero -->
<div class="abs hero" role="img" aria-label="Photo of the spa reception counter with service posters and plants"></div>
<div class="abs hero-shade"></div>
<div class="abs logo-box"><div class="mark"></div><div class="name">EBBTIDE<br>HAVEN</div></div>
<div class="abs topbar">
  <span><svg width="13" height="10" viewBox="0 0 13 10"><rect width="13" height="10" rx="1" fill="#fff"/><path d="M0 1l6.5 5L13 1" stroke="#7082d0" fill="none"/></svg>hello@ebbtidehaven.com.au</span>
  <i class="sep"></i>
  <span><svg width="11" height="11" viewBox="0 0 24 24"><path fill="#fff" d="M6.6 10.8a15 15 0 006.6 6.6l2.2-2.2c.3-.3.7-.4 1-.2 1.1.4 2.3.6 3.6.6.6 0 1 .4 1 1V20c0 .6-.4 1-1 1A17 17 0 013 4c0-.6.4-1 1-1h3.5c.6 0 1 .4 1 1 0 1.2.2 2.4.6 3.6.1.3 0 .7-.2 1z"/></svg>1800 417 305</span>
  <i class="sep"></i>
  <span><svg width="11" height="11" viewBox="0 0 24 24"><circle cx="12" cy="7" r="5" fill="#fff"/><path d="M2 23c0-6 4-9 10-9s10 3 10 9z" fill="#fff"/></svg>Login / Register</span>
</div>
<nav class="abs nav">
  <span>HOME</span><span>FLOAT</span><span>IR SAUNA</span><span>mHBOT</span><span>BIOMAT</span><span>GIFT CARDS</span><span>CONTACT US</span>
  <span class="btn">Book Now <span class="dot"><svg width="8" height="8" viewBox="0 0 8 8"><path d="M3 1l3 3-3 3" stroke="#e8356b" stroke-width="1.4" fill="none"/></svg></span></span>
</nav>
<div class="abs hero-copy">
  <div class="welcome">WELCOME TO</div>
  <h1>EBBTIDE HAVEN</h1>
  <p>Harbour County's First Float Therapy Studio Providing the Ultimate in<br>Relaxation, Meditation, and Recovery, Coral Point, Florida</p>
  <span class="btn">Contact Us <span class="dot"><svg width="8" height="8" viewBox="0 0 8 8"><path d="M3 1l3 3-3 3" stroke="#e8356b" stroke-width="1.4" fill="none"/></svg></span></span>
</div>
<div class="abs scroll-tab"><svg class="abs" style="left:33px;top:12px" width="14" height="24" viewBox="0 0 14 24"><rect x="1" y="1" width="12" height="22" rx="6" stroke="#7082d0" stroke-width="1.5" fill="none"/><line x1="7" y1="6" x2="7" y2="10" stroke="#7082d0" stroke-width="1.5"/></svg></div>

<!-- Mission -->
<section class="abs mission">
  <h2 class="heading">OUR <b>MISSION</b></h2>
  <p class="lead">Our mission is to provide a purpose-built space for our clients to relax, recover and optimise their health. Ebbtide Haven<br>offers Flotation Therapy, Mild Hyperbaric Oxygen Therapy (mHBOT), Infrared Sauna and Biomat sessions.</p>
  <p class="sub">To help us serve and provide real value to our clients we offer membership and bulk booking<br>discounts, as well as great offers in-store.</p>
  <span class="btn">Contact Us <span class="dot"><svg width="8" height="8" viewBox="0 0 8 8"><path d="M3 1l3 3-3 3" stroke="#e8356b" stroke-width="1.4" fill="none"/></svg></span></span>
</section>

<!-- Quick booking -->
<section class="abs quick">
  <div class="abs photo" role="img" aria-label="Photo of the reception desk with brochures and a potted plant"></div>
  <div class="abs band"></div>
  <div class="abs copy">
    <h2>QUICK <b>BOOKING</b></h2>
    <p>Click on the booking above if you know exactly what you want, otherwise feel free to browse below for more info.</p>
    <span class="btn">Book Now <span class="dot"><svg width="8" height="8" viewBox="0 0 8 8"><path d="M3 1l3 3-3 3" stroke="#e8356b" stroke-width="1.4" fill="none"/></svg></span></span>
  </div>
</section>

<!-- Services -->
<h2 class="abs heading services-title">OUR <b>SERVICES</b></h2>
<article class="abs card" style="left:141px">
  <div class="img" role="img" aria-label="Photo of a guest floating in a white float pod" style="background:linear-gradient(135deg,#efeef6,#b7b6e4 55%,#7c6fd0)"></div>
  <div class="icon"><svg width="26" height="22" viewBox="0 0 26 22"><path d="M2 15c4-4 8 4 12 0s8 4 10 0" stroke="#a556a9" stroke-width="2" fill="none"/><circle cx="17" cy="6" r="3" fill="#e8356b"/></svg></div>
  <h3>FLOAT</h3>
  <p>Relax, recharge and replenish.<br>Simple.</p>
</article>
<article class="abs card" style="left:376px">
  <div class="img" role="img" aria-label="Photo of a guest relaxing in an infrared sauna" style="background:linear-gradient(135deg,#c9405f,#e97a8e 50%,#f3c3c9)"></div>
  <div class="icon"><svg width="26" height="22" viewBox="0 0 26 22"><path d="M7 2v6M13 1v7M19 2v6" stroke="#e8356b" stroke-width="2"/><rect x="4" y="12" width="18" height="6" rx="2" fill="#a556a9"/></svg></div>
  <h3>IR SAUNA</h3>
  <p>Turbocharge your detox with our Infrared Sauna.</p>
</article>
<article class="abs card" style="left:610px">
  <div class="img" role="img" aria-label="Photo of a blue hyperbaric oxygen chamber" style="background:linear-gradient(135deg,#2a2c3a,#1e49b8 50%,#6c8fe0)"></div>
  <div class="icon"><svg width="26" height="22" viewBox="0 0 26 22"><circle cx="10" cy="13" r="7" stroke="#e8356b" stroke-width="2" fill="none"/><path d="M17 4h5l-5 5h5" stroke="#a556a9" stroke-width="1.6" fill="none"/></svg></div>
  <h3>mHBOT</h3>
  <p>Mild Hyperbaric Oxygen Therapy, oxygen powered healing.</p>
</article>
<article class="abs card" style="left:845px">
  <div class="img" role="img" aria-label="Photo of a guest resting on a crystal mat with eye mask" style="background:linear-gradient(135deg,#c8741f,#e6a04e 55%,#7a5134)"></div>
  <div class="icon"><svg width="26" height="22" viewBox="0 0 26 22"><path d="M6 2v5M12 1v6M18 2v5" stroke="#a556a9" stroke-width="2"/><rect x="3" y="11" width="20" height="4" fill="#e8356b"/><path d="M4 15v5M22 15v5" stroke="#e8356b" stroke-width="2"/></svg></div>
  <h3>BIOMAT</h3>
  <p>Far Infrared Rays, Negative Ions and Amethyst Crystals all at the same time.</p>
</article>

<!-- Gift card -->
<section class="abs gift">
  <div class="abs photo" role="img" aria-label="Photo of a brochure stand, aroma diffuser and potted plant on a desk"></div>
  <div class="abs band"></div>
  <div class="abs copy">
    <h2>GIFT <b>CARD</b></h2>
    <p>Give the gift of relaxation this festive season<br>with an Ebbtide Haven Gift Card</p>
    <span class="btn">Buy Gift Card <span class="dot"><svg width="8" height="8" viewBox="0 0 8 8"><path d="M3 1l3 3-3 3" stroke="#e8356b" stroke-width="1.4" fill="none"/></svg></span></span>
  </div>
</section>

<!-- Hours & pricing -->
<h2 class="abs heading hp-title">HOURS &amp; <b>PRICING</b></h2>
<div class="abs table hours" style="left:141px">
  <div class="head" role="img" aria-label="Hours">HOURS</div>
  <div class="grid">
    <div class="cell"><h4>Early Sessions</h4><span>6am – 9am</span></div>
    <div class="cell"><h4>Normal Sessions</h4><span>9am – 5pm</span></div>
    <div class="cell"><h4>Late Sessions</h4><span>5pm - 10pm</span></div>
    <div class="cell"><span>We open earlier and stay<br>open longer, just for you.</span></div>
  </div>
</div>
<div class="abs table pricing" style="left:611px">
  <div class="head" role="img" aria-label="Pricing">PRICING</div>
  <div class="grid">
    <div class="cell"><h4>60 min Float Tank</h4><span>$65.00</span></div>
    <div class="cell"><h4>30 min IR Sauna</h4><span>$40.00</span></div>
    <div class="cell"><h4>45 min BioMat</h4><span>$45.00</span></div>
    <div class="cell"><h4>60 min mHBOT</h4><span>$70.00</span></div>
    <div class="cell"><h4>Membership*</h4><span>$25.00 per month</span></div>
    <div class="cell"><span>$20 off every booking!</span></div>
  </div>
</div>

<!-- Map -->
<div class="abs map" role="img" aria-label="Street map showing the centre location in Kelsworth"></div>

<!-- Footer -->
<footer class="abs footer">
  <div class="abs flogo"><div class="mark"></div><div class="name">EBBTIDE<br>HAVEN</div></div>
  <div class="abs fdiv" style="left:275px"></div>
  <div class="abs fcol" style="left:327px">
    <h5>Quick Links</h5>
    <ul><li>Home</li><li>Float</li><li>Ir Sauna</li><li>mHBOT</li><li>Biomat</li><li>Gift Cards</li><li>Contact Us</li></ul>
  </div>
  <div class="abs fdiv" style="left:466px"></div>
  <div class="abs fcol" style="left:518px">
    <h5>Contact Us</h5>
    <div class="crow"><svg width="10" height="14" viewBox="0 0 10 14"><path d="M5 0a5 5 0 015 5c0 4-5 9-5 9S0 9 0 5a5 5 0 015-5z" fill="#fff"/><circle cx="5" cy="5" r="2" fill="#7082d0"/></svg><span>Unit 4/88 Tidewater Road,<br>Kelsworth, QLD, 4512</span></div>
    <div class="crow"><svg width="13" height="10" viewBox="0 0 13 10"><rect width="13" height="10" rx="1" fill="#fff"/><path d="M0 1l6.5 5L13 1" stroke="#7082d0" fill="none"/></svg><span>admin@ebbtidehaven.com.au</span></div>
    <div class="crow"><svg width="12" height="12" viewBox="0 0 24 24"><path fill="#fff" d="M6.6 10.8a15 15 0 006.6 6.6l2.2-2.2c.3-.3.7-.4 1-.2 1.1.4 2.3.6 3.6.6.6 0 1 .4 1 1V20c0 .6-.4 1-1 1A17 17 0 013 4c0-.6.4-1 1-1h3.5c.6 0 1 .4 1 1 0 1.2.2 2.4.6 3.6.1.3 0 .7-.2 1z"/></svg><span>1800 417 305</span></div>
  </div>
  <div class="abs fdiv" style="left:781px"></div>
  <div class="abs fcol" style="left:834px">
    <h5>Subscribe Newsletter</h5>
    <div class="subscribe">Enter Your Email* <span class="go"></span></div>
    <h5 style="margin-top:18px">Social Links</h5>
    <div class="social"><span></span><span></span></div>
  </div>
  <div class="abs copyright">Copyright 2019 Ebbtide Haven . All Rights Reserved.</div>
</footer>

<!-- Contact form card, layered over map and footer -->
<section class="abs contact">
  <h2 class="heading">CONTACT <b>US</b></h2>
  <div class="field" style="left:36px;top:96px;width:272px">Name*</div>
  <div class="field" style="left:327px;top:96px;width:272px">Email*</div>
  <div class="field" style="left:36px;top:146px;width:272px">Phone*</div>
  <div class="field" style="left:327px;top:146px;width:272px">Subject*</div>
  <div class="field" style="left:36px;top:196px;width:563px;height:92px">Message*</div>
  <span class="btn">Submit <span class="dot"><svg width="8" height="8" viewBox="0 0 8 8"><path d="M3 1l3 3-3 3" stroke="#e8356b" stroke-width="1.4" fill="none"/></svg></span></span>
</section>

</body>
</html>
```